Vantrel Web Services

This is a new It services company operating in Perth western Australia

we need a website that is easy to navigate without a cluttered feel to it it should have the following links and pages

About Us
Services
Clients
Contact Us
MY Vantrel (login for clients)

Hi it is a web based IT services company so we would expect customers to come to the website for 2 different purposes the first is to enquire about our services and then as they become customers come to our website to manage their services so whilst they are seperate we want do not want it to look like 2 different websites

hope this helps

Hi to update this we need a home page and templates for sub pages

this is a design brief only and not the coding of the pages or building of the site

```html
<!DOCTYPE html>
<html lang="en">
<head>
<meta charset="utf-8">
<title>Vantrel Web Services</title>
<link href="https://fonts.googleapis.com/css2?family=Michroma&family=Arimo:wght@400;700&family=Open+Sans:wght@400;600&display=swap" rel="stylesheet">
<style>
:root{
  --red:#c4070d;
  --red-dark:#9d0308;
  --ink:#333;
  --muted:#777;
  --white:#fff;
  --band:rgba(20,20,20,.82);
  --grey-bg:#f0f0f0;
  --line:#d6d6d6;
}
*{box-sizing:border-box;margin:0;padding:0}
html,body{width:1050px;height:1200px;overflow:hidden}
body{position:relative;background:var(--white);font-family:"Arimo",Arial,sans-serif;color:var(--ink)}
.abs{position:absolute}
.display{font-family:"Michroma","Arimo",sans-serif;text-transform:uppercase}

/* header */
.site-header{left:0;top:0;width:1050px;height:80px;background:var(--white);z-index:3}
.brand{left:150px;top:14px;display:flex;align-items:center;gap:14px}
.brand-dot{width:54px;height:54px;border-radius:50%;background:var(--red)}
.brand-name{font-family:"Michroma",sans-serif;font-size:25px;color:var(--red);letter-spacing:1px}
.util-nav{right:140px;top:11px;display:flex;gap:14px;font-size:8.5px;color:#666;font-family:"Open Sans",sans-serif;align-items:center}
.util-nav .lang{font-weight:600;color:#444}
.util-nav .phone{font-weight:600;color:#444;margin-left:6px}
.main-nav{left:531px;top:44px;display:flex;gap:17px;font-family:"Open Sans",sans-serif;font-size:11.5px;color:#444}
.btn-red{display:flex;align-items:center;justify-content:center;gap:5px;background:linear-gradient(#e0141a,var(--red-dark));color:var(--white);font-family:"Michroma",sans-serif;font-size:8.5px;text-transform:uppercase;border-radius:2px;box-shadow:0 2px 2px rgba(0,0,0,.35)}
.account-btn{left:780px;top:34px;width:121px;height:35px}

/* hero */
.hero-photo{left:0;top:80px;width:1050px;height:383px;background:radial-gradient(ellipse at 20% 35%,#cfcfcf,#8a8a8a 60%,#6a6a6a),linear-gradient(90deg,#bbb,#888)}
.hero-band{left:0;top:215px;width:1050px;height:145px;background:var(--band)}
.hero-title{left:161px;top:233px;font-size:16px;color:var(--white);letter-spacing:1px}
.hero-copy{left:161px;top:265px;width:470px;font-size:10px;line-height:12.5px;color:#eee}
.login-title{left:682px;top:233px;font-size:16px;color:var(--white);letter-spacing:1px}
.field{left:684px;width:192px;height:26px;background:#ececec;border:1px solid #ccc;font-size:10.5px;color:#333;padding:6px 9px}
.remember{left:684px;top:329px;display:flex;align-items:center;gap:5px;font-size:8.5px;color:#ddd}
.remember i{width:13px;height:13px;background:var(--white);display:block}
.login-btn{left:787px;top:323px;width:89px;height:26px}

/* services */
.service{width:160px;text-align:center}
.service .disc{width:118px;height:118px;border-radius:50%;background:var(--white);margin:0 auto;display:flex;align-items:flex-start;justify-content:center;padding-top:26px}
.service h3{font-family:"Michroma",sans-serif;font-size:8.5px;line-height:14px;color:var(--red);text-transform:uppercase;margin-top:-28px}
.service p{font-size:10.3px;line-height:12.5px;color:#444;margin-top:14px}
.service-card{left:358px;top:462px;width:166px;height:161px;background:var(--white);box-shadow:0 1px 6px rgba(0,0,0,.28)}
.read-more{left:387px;top:581px;width:108px;height:26px;border:1px solid #e2e2e2;box-shadow:0 1px 3px rgba(0,0,0,.15);font-family:"Michroma",sans-serif;font-size:8px;color:var(--red);display:flex;align-items:center;justify-content:center;background:var(--white)}

/* promo */
.promo-photo{left:0;top:651px;width:1050px;height:302px;background:linear-gradient(90deg,#6e4e6e 0%,#8f6680 35%,#a7788a 60%,#9a6c7d 100%)}
.promo-title{left:500px;top:716px;width:390px;text-align:center;font-size:17px;line-height:27px;color:var(--white);letter-spacing:1px}
.promo-copy{left:525px;top:803px;width:340px;text-align:center;font-size:10.5px;line-height:13px;color:#eadde4}
.signup-btn{left:571px;top:849px;width:121px;height:35px}
.contact-btn{left:698px;top:849px;width:121px;height:35px}

/* customers */
.customers{left:0;top:953px;width:1050px;height:169px;background:var(--grey-bg)}
.customers h2{position:absolute;left:0;top:35px;width:1050px;text-align:center;font-size:11px;color:#222;letter-spacing:1px}
.customers .rule{position:absolute;left:155px;top:53px;width:741px;height:1px;background:var(--line)}
.customer-list{position:absolute;left:155px;top:95px;width:741px;display:flex;justify-content:space-between;align-items:center;padding:0 18px}
.customer{display:flex;align-items:center;gap:6px;font-family:"Arimo",sans-serif;font-weight:700;font-size:15px;color:#8d8d8d}
.customer i{width:16px;height:16px;background:#9c9c9c;display:block}
.customer i.round{border-radius:50%}

/* footer */
.footer-brand{left:157px;top:1143px;display:flex;align-items:center;gap:6px}
.footer-brand .brand-dot{width:18px;height:18px}
.footer-brand .brand-name{font-size:10px;letter-spacing:.5px}
.footer-meta{left:156px;top:1166px;font-size:8.5px;color:#888;white-space:nowrap}
.footer-meta span{margin:0 8px;color:#aaa}
.social{left:770px;top:1154px;display:flex;gap:6px}
.social i{width:15px;height:15px;display:block;border-radius:2px}
</style>
</head>
<body>

<header class="site-header abs">
  <div class="brand abs">
    <span class="brand-dot"></span>
    <span class="brand-name">Vantrel</span>
  </div>
  <nav class="util-nav abs">
    <span>Login</span><span>Help</span><span>Cookies</span><span>Policy</span>
    <span class="lang">English ▾</span>
    <span class="phone">1-555-014-2200
      <svg width="9" height="9" viewBox="0 0 10 10"><path d="M2 1l2 2-1 1.3a6 6 0 0 0 2.7 2.7L7 6l2 2-1.3 1.5C4.5 9.4.6 5.5.5 2.3z" fill="#999"/></svg>
    </span>
  </nav>
  <nav class="main-nav abs">
    <span>About Us</span><span>Services</span><span>Clients</span><span>Contact Us</span>
  </nav>
  <a class="btn-red account-btn abs">
    <svg width="9" height="9" viewBox="0 0 10 10"><circle cx="5" cy="3" r="2.4" fill="#fff"/><path d="M0.8 10a4.2 4 0 0 1 8.4 0z" fill="#fff"/></svg>MY Vantrel
  </a>
</header>

<div class="hero-photo abs" role="img" aria-label="Greyscale photo of a globe, binary code, a padlock and circuit board"></div>
<div class="hero-band abs"></div>
<h1 class="hero-title display abs">Web Based IT Services</h1>
<p class="hero-copy abs">Lorem ipsum dolor sit amet, consectetuer adipiscing elit, sed diam nonummy nibh euismod tincidunt ut laoreet dolore magna aliquam erat volutpat. Ut wisi enim ad minim veniam, quis nostrud exerci tation ullamcorper suscipit lobortis nisl ut aliquip ex ea commodo consequat. Duis autem vel eum iriure dolor in hendrerit in vulputate velit esse molestie consequat, vel illum dolore eu feugiat nulla facilisis at vero eros et accumsan et iusto odio dignissim qui blandit praesent luptatum zzril delenit augue duis dolore te feugait nulla facilisi.</p>

<h2 class="login-title display abs">Customer Login</h2>
<div class="field abs" style="top:265px">Username</div>
<div class="field abs" style="top:293px">Password</div>
<label class="remember abs"><i></i>Save Password</label>
<a class="btn-red login-btn abs">Login</a>

<div class="service-card abs"></div>

<section class="service abs" style="left:188px;top:386px">
  <div class="disc">
    <svg width="40" height="44" viewBox="0 0 40 44"><path d="M8 20a12 12 0 0 1 24 0" stroke="#c4070d" stroke-width="3" fill="none"/><circle cx="20" cy="19" r="9" fill="#c4070d"/><rect x="5" y="18" width="6" height="10" rx="2" fill="#c4070d"/><rect x="29" y="18" width="6" height="10" rx="2" fill="#c4070d"/><path d="M2 44c1-10 8-14 18-14s17 4 18 14z" fill="#c4070d"/></svg>
  </div>
  <h3>Customer<br>Support</h3>
  <p>Ut wisi enim ad minim veniam, quis nostrud exerci tation ullamcorper suscipit lobortis nisl ut aliquip ex ea commodo consequat.</p>
</section>

<section class="service abs" style="left:361px;top:386px">
  <div class="disc">
    <svg width="44" height="44" viewBox="0 0 44 44"><circle cx="22" cy="22" r="16" fill="none" stroke="#c4070d" stroke-width="6" stroke-dasharray="5 3.4"/><circle cx="22" cy="22" r="11" fill="#c4070d"/><path d="M11 22h22M22 11v22M15 15q7 7 14 0M15 29q7-7 14 0" stroke="#fff" stroke-width="1.3" fill="none"/></svg>
  </div>
  <h3 style="margin-top:-26px">Application<br>Development</h3>
  <p>Lorem ipsum dolor sit amet, consectetuer adipiscing elit, sed diam nonummy nibh euismod tincidunt ut laoreet dolore magna…</p>
</section>
<a class="read-more abs">read more ››</a>

<section class="service abs" style="left:531px;top:386px">
  <div class="disc">
    <svg width="46" height="46" viewBox="0 0 46 46"><rect x="2" y="10" width="40" height="26" rx="2" fill="none" stroke="#c4070d" stroke-width="3"/><path d="M18 37v5h10v-5M14 44h18" stroke="#c4070d" stroke-width="3" fill="none"/><rect x="14" y="2" width="14" height="22" rx="2" fill="#c4070d"/><rect x="30" y="14" width="12" height="16" rx="2" fill="#c4070d"/></svg>
  </div>
  <h3 style="margin-top:-26px">Application<br>Management</h3>
  <p>Duis autem vel eum iriure dolor in hendrerit in vulputate velit esse molestie consequat, vel illum dolore eu feugiat nulla …</p>
</section>

<section class="service abs" style="left:701px;top:386px">
  <div class="disc">
    <svg width="40" height="46" viewBox="0 0 40 46"><circle cx="12" cy="8" r="6" fill="#c4070d"/><path d="M2 44V24a8 8 0 0 1 8-8h6a8 8 0 0 1 6 3v25z" fill="#c4070d"/><circle cx="29" cy="33" r="8" fill="none" stroke="#c4070d" stroke-width="5" stroke-dasharray="3 2.3"/><circle cx="29" cy="33" r="5" fill="#c4070d"/><circle cx="29" cy="33" r="2" fill="#fff"/></svg>
  </div>
  <h3 style="margin-top:-26px">Business and<br>IT Consulting</h3>
  <p>Facilisis at vero eros et accumsan et iusto odio dignissim qui blandit praesent luptatum zzril delenit augue duis dolore te feugait nulla facilisi.</p>
</section>

<div class="promo-photo abs" role="img" aria-label="Photo of a joyful businessman with a laptop, arms raised against a dusky pink sky"></div>
<h2 class="promo-title display abs">This could be the beginning of a successful business .</h2>
<p class="promo-copy abs">Duis autem vel eum iriure dolor in hendrerit in vulputate velit esse molestie consequat, vel illum dolore eu feugiat nulla …</p>
<a class="btn-red signup-btn abs">
  <svg width="11" height="10" viewBox="0 0 11 10"><circle cx="4" cy="3" r="2.4" fill="#fff"/><path d="M0 10a4 4 0 0 1 8 0z" fill="#fff"/><circle cx="8.5" cy="7.5" r="2" fill="none" stroke="#fff"/></svg>Sign up
</a>
<a class="btn-red contact-btn abs">
  <svg width="11" height="8" viewBox="0 0 11 8"><rect width="11" height="8" fill="#fff"/><path d="M0 0l5.5 4.5L11 0" stroke="#c4070d" fill="none"/></svg>Contact
</a>

<section class="customers abs">
  <h2 class="display">Our Customers</h2>
  <div class="rule"></div>
  <div class="customer-list">
    <span class="customer">Norvella</span>
    <span class="customer"><i class="round"></i>Lumary</span>
    <span class="customer"><i></i>Quillon Tech</span>
    <span class="customer"><i></i>Ostrek</span>
    <span class="customer">Caldera Labs</span>
    <span class="customer"><i class="round"></i>Pivona</span>
  </div>
</section>

<footer>
  <div class="footer-brand abs">
    <span class="brand-dot"></span>
    <span class="brand-name">Vantrel</span>
  </div>
  <p class="footer-meta abs">Privacy Policy<span>|</span>Terms &amp; Conditions<span>|</span>Vantrel Pty Ltd - 48 Harbour Row, Level 2 - Perth - WA 6000 - Australia &nbsp;© Vantrel 2014</p>
  <div class="social abs">
    <i style="background:#3b5a9a"></i>
    <i style="background:#c3202a"></i>
    <i style="background:#2da8de"></i>
    <i style="background:#32a9d0"></i>
    <i style="background:#6fbb3f"></i>
    <i style="background:#e24b87"></i>
  </div>
</footer>

</body>
</html>
```